Commercial Insurance Agency needs a design for a trade show retractable display.

We need a design for a retractable banner or display for a trade show. We are a commercial insurance agency that specializes in placing and servicing workers comp insurance for large companies. We want to use our company colors which are orange, grey and charcoal.

Font styles to use
Sans Serif

Requirements
Must have
• Our orange color that is on the style sheet should be the secondary color...we don't want the whole thing to be orange

```html
<!DOCTYPE html>
<html lang="en">
<head>
<meta charset="utf-8">
<title>Harborline – Trade Show Retractable Banner</title>
<link rel="stylesheet" href="https://fonts.googleapis.com/css2?family=Montserrat:wght@500;700&display=swap">
<style>
  :root {
    --orange: #f05a22;
    --charcoal: #4a4a4a;
    --ink: #2f2f2f;
    --light-grey: #e4e4e4;
    --text-grey: #d9d9d9;
    --white: #ffffff;
    --backdrop: #ececec;
  }
  html, body {
    margin: 0;
    padding: 0;
    width: 1200px;
    height: 1000px;
    overflow: hidden;
    background: var(--backdrop);
    font-family: "Montserrat", Arial, sans-serif;
  }
  .banner {
    position: absolute;
    left: 385px;
    top: 60px;
    width: 430px;
    height: 880px;
    background: var(--charcoal);
    overflow: hidden;
  }
  .banner__photo {
    position: absolute;
    left: 0;
    top: 14px;
    width: 430px;
    height: 480px;
    background: linear-gradient(160deg, #f2f4f6 0%, #dfe3e7 40%, #c9c1b8 65%, #6b6f78 100%);
  }
  .banner__top-band {
    position: absolute;
    left: 0;
    top: 0;
    width: 430px;
    height: 14px;
    background: var(--orange);
  }
  .banner__shapes {
    position: absolute;
    left: 0;
    top: 0;
  }
  .brand-name {
    position: absolute;
    left: 150px;
    top: 322px;
    margin: 0;
    color: var(--ink);
    font-weight: 700;
    font-size: 36px;
    line-height: 1;
    letter-spacing: 0.5px;
  }
  .service {
    position: absolute;
    color: var(--text-grey);
    font-size: 13px;
    line-height: 17px;
    font-weight: 500;
  }
  .service__title {
    color: var(--orange);
    font-weight: 700;
    font-size: 19px;
    line-height: 22px;
    margin: 0 0 2px;
    letter-spacing: 0.3px;
  }
  .service__text { margin: 0; }
  .service--compliance { left: 165px; top: 492px; width: 240px; }
  .service--claims { left: 40px; top: 619px; width: 206px; text-align: right; }
  .service--profit { left: 162px; top: 727px; width: 250px; }
  .banner__footer {
    position: absolute;
    left: 0;
    bottom: 0;
    width: 430px;
    height: 40px;
    background: var(--orange);
    color: var(--white);
    font-weight: 500;
    font-size: 17px;
    display: flex;
    align-items: center;
    justify-content: center;
  }
</style>
</head>
<body>
  <div class="banner">
    <div class="banner__photo" role="img" aria-label="Photo of two business professionals in a meeting at a bright office desk"></div>
    <div class="banner__top-band"></div>

    <svg class="banner__shapes" width="430" height="880" viewBox="0 0 430 880" aria-hidden="true">
      <polygon points="0,462 390,396 430,396 430,482 0,506" fill="var(--orange)"/>
      <line x1="0" y1="496" x2="398" y2="430" stroke="var(--white)" stroke-width="3"/>
      <polygon points="0,503 396,438 430,482 430,880 0,880" fill="var(--charcoal)"/>

      <g transform="translate(88,525)">
        <circle r="58" fill="var(--orange)"/>
        <circle r="53" fill="var(--white)"/>
        <circle r="47" fill="var(--light-grey)"/>
        <g fill="var(--orange)">
          <circle r="24"/>
          <rect x="-5" y="-32" width="10" height="12"/>
          <rect x="-5" y="20" width="10" height="12"/>
          <rect x="-32" y="-5" width="12" height="10"/>
          <rect x="20" y="-5" width="12" height="10"/>
          <rect x="-5" y="-32" width="10" height="12" transform="rotate(45)"/>
          <rect x="-5" y="20" width="10" height="12" transform="rotate(45)"/>
          <rect x="-32" y="-5" width="12" height="10" transform="rotate(45)"/>
          <rect x="20" y="-5" width="12" height="10" transform="rotate(45)"/>
        </g>
        <circle r="14" fill="var(--light-grey)"/>
        <line x1="-6" y1="-6" x2="18" y2="18" stroke="var(--orange)" stroke-width="7" stroke-linecap="round"/>
        <circle cx="-8" cy="-8" r="8" fill="var(--orange)"/>
      </g>

      <g transform="translate(322,645)">
        <circle r="58" fill="var(--orange)"/>
        <circle r="53" fill="var(--white)"/>
        <circle r="47" fill="var(--light-grey)"/>
        <path d="M-22,-6 A23,23 0 0 1 16,-18" fill="none" stroke="var(--orange)" stroke-width="7"/>
        <polygon points="10,-28 28,-22 16,-6" fill="var(--orange)"/>
        <path d="M22,6 A23,23 0 0 1 -16,18" fill="none" stroke="var(--orange)" stroke-width="7"/>
        <polygon points="-10,28 -28,22 -16,6" fill="var(--orange)"/>
      </g>

      <g transform="translate(88,758)">
        <circle r="58" fill="var(--orange)"/>
        <circle r="53" fill="var(--white)"/>
        <circle r="47" fill="var(--light-grey)"/>
        <g stroke="var(--orange)" stroke-width="3" fill="none" stroke-linecap="round">
          <path d="M-7,14 C-7,4 -15,0 -15,-8 A15,15 0 0 1 15,-8 C15,0 7,4 7,14 Z"/>
          <line x1="-7" y1="19" x2="7" y2="19"/>
          <line x1="-5" y1="24" x2="5" y2="24"/>
          <line x1="0" y1="-32" x2="0" y2="-38"/>
          <line x1="-22" y1="-22" x2="-26" y2="-26"/>
          <line x1="22" y1="-22" x2="26" y2="-26"/>
          <line x1="-30" y1="-6" x2="-36" y2="-6"/>
          <line x1="30" y1="-6" x2="36" y2="-6"/>
        </g>
      </g>
    </svg>

    <p class="brand-name">Harborline</p>

    <div class="service service--compliance">
      <h2 class="service__title">COMPLIANCE</h2>
      <p class="service__text">Training and Certifications HR<br>and Safety Onsite Compliance<br>Audits</p>
    </div>
    <div class="service service--claims">
      <h2 class="service__title">CLAIMS</h2>
      <p class="service__text">Immediate, Ongoing Injury<br>and Claims Management</p>
    </div>
    <div class="service service--profit">
      <h2 class="service__title">PROFIT LEAMS</h2>
      <p class="service__text">Detect and Correct Profit<br>Leaks Inherent in Every Work<br>Comp Program that Drives the Cost</p>
    </div>

    <div class="banner__footer">harborline.com</div>
  </div>
</body>
</html>
```